QM Studios needs and Interior Design Business card

I can do anything from Commercial to Residential and Free lance. Beginning to end in design selection process.
Need something to catch the eye of potential customers and vendors. From furniture to Tile and Cabinet selections. I can do it all.

Industry/Entity Type

Design Agency

Contact Information for Business Card

QM Studios- Design Consultanting Residential, Commerical
Maybe a cool detail background. Wall paper print that can have some texture

Font styles to use
Serif

Colors
709dcb
34a6d7
b868aa
e667a6
f59296
85acd3
ffffff
000000
5c5c5c

Requirements
Must have
• Square or Rectangular with Rounded edges
• Name
• Address
• Phone
• Email
Nice to have
• Some colored edges More simples not too busy
• Pattern detail in background.
Should not have
• Not too much color

```html
<!DOCTYPE html>
<html lang="en">
<head>
<meta charset="UTF-8">
<title>QM Studios – Business Card</title>
<link rel="stylesheet" href="https://fonts.googleapis.com/css2?family=Noticia+Text&family=Questrial&display=swap">
<style>
  :root {
    --page-bg: #ece9e4;
    --card-bg: #ffffff;
    --ink: #1e1b1c;
    --muted: #5c5c5c;
    --accent-pink: #e667a6;
    --card-shadow: rgba(0, 0, 0, 0.35);
  }
  * { margin: 0; padding: 0; box-sizing: border-box; }
  html, body {
    width: 1000px;
    height: 1200px;
    overflow: hidden;
  }
  body {
    position: relative;
    background: var(--page-bg);
    font-family: "Noticia Text", Georgia, serif;
    color: var(--ink);
  }
  .card {
    position: absolute;
    left: 279px;
    width: 442px;
    height: 442px;
    background: var(--card-bg);
    box-shadow: 2px 3px 6px var(--card-shadow);
  }
  .card--front { top: 124px; }
  .card--back { top: 628px; }

  .brand-ring {
    position: absolute;
    border: 5px solid var(--ink);
    border-radius: 50%;
  }
  .card--front .brand-ring {
    left: 62px;
    top: 150px;
    width: 112px;
    height: 112px;
    margin-top: -20px;
  }
  .card--front .brand-name {
    position: absolute;
    left: 38px;
    top: 262px;
    width: 160px;
    text-align: center;
    font-family: "Questrial", Arial, sans-serif;
    font-size: 17px;
    letter-spacing: 3px;
    color: var(--ink);
  }
  .divider {
    position: absolute;
    left: 215px;
    top: 155px;
    width: 1.5px;
    height: 135px;
    background: var(--ink);
  }
  .contact {
    position: absolute;
    left: 232px;
    top: 162px;
  }
  .contact__name {
    font-size: 25px;
    line-height: 32px;
    font-weight: 400;
  }
  .contact__role {
    font-size: 12.5px;
    line-height: 16px;
    margin-bottom: 7px;
  }
  .contact__line {
    display: flex;
    align-items: center;
    font-size: 15px;
    line-height: 21px;
  }
  .contact__icon {
    width: 13px;
    height: 13px;
    margin-right: 6px;
    fill: var(--accent-pink);
  }
  .contact__scope {
    font-size: 11px;
    line-height: 18px;
    margin-left: 19px;
    color: var(--ink);
  }

  .card--back .brand-ring {
    left: 162px;
    top: 137px;
    width: 118px;
    height: 118px;
    border-width: 4px;
  }
  .card--back .brand-name {
    position: absolute;
    left: 0;
    top: 268px;
    width: 100%;
    text-align: center;
    font-family: "Questrial", Arial, sans-serif;
    font-size: 33px;
    letter-spacing: 6px;
    color: var(--ink);
  }
</style>
</head>
<body>
  <section class="card card--front">
    <div class="brand-ring"></div>
    <div class="brand-name">QM Studios</div>
    <div class="divider"></div>
    <div class="contact">
      <h1 class="contact__name">Nora Vellacourt</h1>
      <p class="contact__role">Design Consultant</p>
      <p class="contact__line">
        <svg class="contact__icon" viewBox="0 0 24 24" aria-hidden="true"><path d="M6.6 10.8c1.4 2.8 3.8 5.1 6.6 6.6l2.2-2.2c.3-.3.7-.4 1-.2 1.1.4 2.3.6 3.6.6.6 0 1 .4 1 1V20c0 .6-.4 1-1 1C10.6 21 3 13.4 3 4c0-.6.4-1 1-1h3.5c.6 0 1 .4 1 1 0 1.3.2 2.5.6 3.6.1.3 0 .7-.2 1l-2.3 2.2z"/></svg>
        555-014-2290
      </p>
      <p class="contact__line">
        <svg class="contact__icon" viewBox="0 0 24 24" aria-hidden="true"><path d="M2 5h20v14H2z M2 5l10 8 10-8" /><path d="M2 5l10 8 10-8v2l-10 8L2 7z" fill="#fff"/></svg>
        n.vellacourt@mail.com
      </p>
      <p class="contact__scope">Residential/Commercial</p>
    </div>
  </section>

  <section class="card card--back">
    <div class="brand-ring"></div>
    <div class="brand-name">QM Studios</div>
  </section>
</body>
</html>
```